For Brivo: Business cards, letterhead, envelopes and double sided page

For Brivo: Previously described in email.

Business cards, letterhead, envelopes, and glossy marketing double sided page.

Marketing

```html
<!DOCTYPE html>
<html lang="en">
<head>
<meta charset="utf-8">
<title>Quorvane Letterhead</title>
<link rel="stylesheet" href="https://fonts.googleapis.com/css2?family=Michroma&display=swap">
<style>
  :root {
    --ink: #000000;
    --paper: #ffffff;
    --gold: #e2bb16;
    --gold-light: #efcf2a;
    --rule: #ffffff;
  }
  * { margin: 0; padding: 0; box-sizing: border-box; }
  html, body {
    width: 927px;
    height: 1200px;
    overflow: hidden;
    background: var(--paper);
  }
  .letterhead {
    position: relative;
    width: 927px;
    height: 1200px;
    background: var(--paper);
    font-family: "Michroma", sans-serif;
  }
  .masthead {
    position: absolute;
    left: 0; top: 0;
    width: 100%;
    height: 162px;
    background: var(--ink);
  }
  .brand {
    position: absolute;
    left: 45px;
    top: 58px;
    height: 66px;
    display: flex;
    align-items: center;
    gap: 20px;
  }
  .brand-mark {
    flex: 0 0 auto;
    width: 46px;
    height: 46px;
    background: var(--gold);
  }
  .brand-name {
    color: var(--paper);
    font-size: 46px;
    line-height: 1;
    letter-spacing: 3px;
    white-space: nowrap;
  }
  .masthead-rule {
    position: absolute;
    left: 0; top: 162px;
    width: 100%;
    height: 4px;
    background: var(--rule);
  }
  .address-band {
    position: absolute;
    left: 0; top: 166px;
    width: 100%;
    height: 48px;
    background: linear-gradient(to bottom, var(--gold-light), var(--gold));
  }
  .address {
    position: absolute;
    right: 33px;
    top: 50%;
    transform: translateY(-50%);
    color: var(--ink);
    font-size: 16px;
    line-height: 1;
    letter-spacing: 8px;
    text-transform: uppercase;
    white-space: nowrap;
  }
</style>
</head>
<body>
  <main class="letterhead">
    <header class="masthead">
      <div class="brand">
        <span class="brand-mark" aria-hidden="true"></span>
        <span class="brand-name">Quorvane</span>
      </div>
    </header>
    <div class="masthead-rule"></div>
    <div class="address-band">
      <p class="address">Address will be here</p>
    </div>
  </main>
</body>
</html>
```